brightleafwell.com and torvahealth.com

I'd like to do a web design re-make on two of our websites. Brightleafwell.com is focused on selling nutriceutical products (private labeled by brightleafwell.com), and provide an expert blog to give great advices on general health.

Torvahealth.com is a site for Dr. Moreau's new medicine clinic. It should be integrated with brightleafwell.com. Clients can directly make appointments on the site, and order products from brightleafwell.com.

Target Market(s)

Middle to upper

Industry/Entity Type

Clinic

Number of Pages Required

4 page

Font styles to use
Serif
Sans Serif

Colors
0254a3
0792cd
33a6d7
00a98f
33b7a4
acd036
9bcb3c
cadf82

Requirements
Must have
• Home page tabs: About Dr. Moreau, Store, Blog, Videos, Appointment
• Home page content should include: a promotional section (with moving features), an appointment book (for online appointment booking), a product section (for store), and a blog section.
Nice to have
• The look and feel should be modern, professional, trustworthy, zen.
Should not have
• Real pictures of people, except for Dr. Moreau.

```html
<!DOCTYPE html>
<html lang="en">
<head>
<meta charset="utf-8">
<title>Brightleaf Well — Home</title>
<link href="https://fonts.googleapis.com/css2?family=Open+Sans:wght@400;600;700&display=swap" rel="stylesheet">
<style>
:root{
  --navy:#12386e;
  --text:#555b63;
  --line:#dcdfe3;
  --page:#ffffff;
  --hero-a:#e9f0f7;
  --hero-b:#c9dcee;
  --photo-a:#f1e3d6;
  --photo-b:#d9bfa8;
  --bottle:#eef0f4;
}
*{box-sizing:border-box;margin:0;padding:0}
html,body{width:1200px;height:2375px;overflow:hidden;background:var(--page)}
body{position:relative;font-family:"Open Sans",Arial,sans-serif;color:var(--text)}
a{color:inherit;text-decoration:none}
.abs{position:absolute}

.brand{left:103px;top:44px;width:220px;font-size:30px;font-weight:700;color:var(--navy);line-height:1.05;letter-spacing:-.5px}
.cart-btn{left:943px;top:19px;width:154px;height:38px;background:var(--navy);border-radius:3px;color:#fff;font-size:14px;display:flex;align-items:center;justify-content:center;gap:8px}
.main-nav{right:103px;top:89px;display:flex;gap:41px;font-size:13px;color:#4a4f56;text-transform:uppercase}
.main-nav .current{color:var(--navy)}

.hero{left:103px;top:146px;width:994px;height:551px;overflow:hidden;background:radial-gradient(circle at 25% 30%,#ffffff 0,var(--hero-a) 35%,var(--hero-b) 100%)}
.hero-portrait{position:absolute;left:410px;top:0;width:584px;height:551px;background:radial-gradient(ellipse at 55% 45%,#eed8c8 0,#d9b9a3 40%,rgba(201,220,238,0) 75%)}
.hero h1{position:absolute;left:36px;top:183px;font-size:35px;line-height:47px;font-weight:700;color:var(--navy)}
.hero p{position:absolute;left:37px;top:290px;width:425px;font-size:14.5px;line-height:24px;letter-spacing:-.1px;color:var(--text)}
.btn{background:var(--navy);color:#fff;border-radius:3px;display:flex;align-items:center;justify-content:center}
.hero .btn{position:absolute;left:38px;top:387px;width:158px;height:45px;font-size:16px}
.dots{position:absolute;left:38px;top:498px;display:flex;gap:3px}
.dots span{width:11px;height:11px;border-radius:50%;background:#555}
.dots span:first-child{background:var(--navy)}

.section-title{font-size:27px;font-weight:700;color:var(--navy)}

.product{width:220px;text-align:center}
.product-frame{height:221px;border:1px solid var(--line);display:flex;align-items:center;justify-content:center}
.product-shot{width:72px;height:140px;border-radius:14px 14px 8px 8px;background:linear-gradient(90deg,#d6dae2,var(--bottle) 40%,#d2d6de)}
.product-name{margin-top:28px;font-size:17px;font-weight:600;color:#4a4f56}
.product-price{margin-top:12px;font-size:17px;font-weight:700;color:#4a4f56}
.product .btn{margin:14px auto 0;width:159px;height:42px;font-size:14px;gap:10px}

.post{left:103px;width:592px;height:257px;border:1px solid var(--line)}
.post-photo{position:absolute;left:25px;top:26px;width:200px;height:201px;background:linear-gradient(135deg,var(--photo-a),var(--photo-b))}
.post-body{position:absolute;left:245px;top:34px;width:330px}
.post-body h3{font-size:17px;font-weight:700;color:var(--navy)}
.post-body p{margin-top:9px;font-size:14px;line-height:24.5px;letter-spacing:-.15px;color:var(--text)}
.post-body a{display:block;margin-top:9px;font-size:14px;color:var(--navy)}

.pager{left:103px;top:2142px;display:flex;gap:9px;font-size:12px;font-weight:700;color:#333}
.pager span{height:28px;min-width:28px;padding:0 8px;border:1px solid var(--line);border-radius:2px;display:flex;align-items:center;justify-content:center;background:#fafafa}
.pager .page{font-weight:400;font-size:11px}
.pager .wide{min-width:57px;font-size:13px}

.widget{left:744px;width:353px;border:1px solid var(--line)}
.widget-head{height:66px;background:var(--navy);color:#fff;font-size:20px;font-weight:700;display:flex;align-items:center;justify-content:space-between;padding:0 20px 0 18px}
.field{margin:17px 16px 0;height:42px;border:1px solid var(--line);font-size:13.5px;color:#666;display:flex;align-items:center;justify-content:space-between;padding:0 12px}
.field + .field{margin-top:15px}
.widget .book{margin:15px auto 0;width:121px;height:41px;font-size:15px}

.promo-list{padding-top:22px}
.promo-item{display:flex;gap:18px;margin:0 0 25px 19px}
.promo-shot{flex:none;width:107px;height:100px;border:1px solid var(--line);display:flex;align-items:center;justify-content:center}
.promo-shot div{width:36px;height:68px;border-radius:8px 8px 4px 4px;background:linear-gradient(90deg,#d6dae2,var(--bottle) 40%,#d2d6de)}
.promo-text h4{font-size:15.5px;font-weight:700;color:var(--navy)}
.promo-text p{margin-top:4px;font-size:13px;line-height:24px;color:var(--text);width:180px}
.promo-text a{display:block;margin-top:2px;font-size:13px;color:var(--navy)}

.footer{left:0;top:2237px;width:1200px;height:138px;background:var(--navy);color:#fff}
.footer-nav{position:absolute;left:103px;top:34px;font-size:14px;display:flex;gap:20px}
.copyright{position:absolute;left:103px;top:83px;font-size:14px}
.social{position:absolute;right:103px;top:27px;display:flex;gap:9px}
.social span{width:32px;height:32px;border-radius:50%;background:#fff}
</style>
</head>
<body>

<header>
  <div class="abs brand">Brightleaf<br>Well</div>
  <a class="abs cart-btn" href="#">
    <svg width="22" height="18" viewBox="0 0 22 18" fill="none" stroke="#fff" stroke-width="1.8"><path d="M1 2h3l3 10h11l2-7H6"/><circle cx="9" cy="15.5" r="1.4" fill="#fff"/><circle cx="17" cy="15.5" r="1.4" fill="#fff"/></svg>
    Cart is empty
  </a>
  <nav class="abs main-nav">
    <a class="current" href="#">Home</a><a href="#">About Dr.Ardel</a><a href="#">Store</a><a href="#">Blog</a><a href="#">Videos</a><a href="#">Appointment</a>
  </nav>
</header>

<section class="abs hero">
  <div class="hero-portrait" role="img" aria-label="Portrait of a woman with clear skin against a soft blue background"></div>
  <h1>Empowering Your<br>Ageless Body And Mind</h1>
  <p>Lorem ipsum dolor sit amet, summo vocent dolores sit ne, ne tale saepe invenire duo, ancillae noluisse per eu. Sea ex decore invidunt mediocrem, per te vidit ludus vocibu.</p>
  <a class="btn" href="#">Read More</a>
  <div class="dots"><span></span><span></span><span></span><span></span></div>
</section>

<h2 class="abs section-title" style="left:103px;top:729px">Our Products</h2>
<div class="abs product" style="left:103px;top:792px">
  <div class="product-frame"><div class="product-shot" role="img" aria-label="Candaclear supplement bottle"></div></div>
  <div class="product-name">Candaclear</div><div class="product-price">$40.00</div>
  <a class="btn" href="#"><svg width="22" height="18" viewBox="0 0 22 18" fill="none" stroke="#fff" stroke-width="1.8"><path d="M1 2h3l3 10h11l2-7H6"/><circle cx="9" cy="15.5" r="1.4" fill="#fff"/><circle cx="17" cy="15.5" r="1.4" fill="#fff"/></svg>Add To Cart</a>
</div>
<div class="abs product" style="left:361px;top:792px">
  <div class="product-frame"><div class="product-shot" role="img" aria-label="Radiance Well supplement bottle"></div></div>
  <div class="product-name">Radiance Well</div><div class="product-price">$40.00</div>
  <a class="btn" href="#"><svg width="22" height="18" viewBox="0 0 22 18" fill="none" stroke="#fff" stroke-width="1.8"><path d="M1 2h3l3 10h11l2-7H6"/><circle cx="9" cy="15.5" r="1.4" fill="#fff"/><circle cx="17" cy="15.5" r="1.4" fill="#fff"/></svg>Add To Cart</a>
</div>
<div class="abs product" style="left:619px;top:792px">
  <div class="product-frame"><div class="product-shot" role="img" aria-label="AdrenaVita supplement bottle"></div></div>
  <div class="product-name">AdrenaVita</div><div class="product-price">$40.00</div>
  <a class="btn" href="#"><svg width="22" height="18" viewBox="0 0 22 18" fill="none" stroke="#fff" stroke-width="1.8"><path d="M1 2h3l3 10h11l2-7H6"/><circle cx="9" cy="15.5" r="1.4" fill="#fff"/><circle cx="17" cy="15.5" r="1.4" fill="#fff"/></svg>Add To Cart</a>
</div>
<div class="abs product" style="left:877px;top:792px">
  <div class="product-frame"><div class="product-shot" role="img" aria-label="Allerpeace supplement bottle"></div></div>
  <div class="product-name">Allerpeace</div><div class="product-price">$40.00</div>
  <a class="btn" href="#"><svg width="22" height="18" viewBox="0 0 22 18" fill="none" stroke="#fff" stroke-width="1.8"><path d="M1 2h3l3 10h11l2-7H6"/><circle cx="9" cy="15.5" r="1.4" fill="#fff"/><circle cx="17" cy="15.5" r="1.4" fill="#fff"/></svg>Add To Cart</a>
</div>

<h2 class="abs section-title" style="left:103px;top:1197px">Our Blog</h2>
<article class="abs post" style="top:1263px">
  <div class="post-photo" role="img" aria-label="Photo of a smiling woman"></div>
  <div class="post-body"><h3>Lorem ipsum dolor</h3><p>Lorem ipsum dolor sit amet, at vel eruditi inve&shy;nire elaboraret, quo commune consequuntur ne. No gubergren prodesset cum, mea alia noster perpetua an, pri nisl fuisset an. No guber&shy;gren prodesset cum, mea alia noster.</p><a href="#">[Read More]</a></div>
</article>
<article class="abs post" style="top:1555px">
  <div class="post-photo" role="img" aria-label="Photo of a woman relaxing during a massage"></div>
  <div class="post-body"><h3>Lorem ipsum dolor</h3><p>Lorem ipsum dolor sit amet, at vel eruditi inve&shy;nire elaboraret, quo commune consequuntur ne. No gubergren prodesset cum, mea alia noster perpetua an, pri nisl fuisset an. No guber&shy;gren prodesset cum, mea alia noster.</p><a href="#">[Read More]</a></div>
</article>
<article class="abs post" style="top:1846px">
  <div class="post-photo" role="img" aria-label="Photo of a woman touching her face"></div>
  <div class="post-body"><h3>Lorem ipsum dolor</h3><p>Lorem ipsum dolor sit amet, at vel eruditi inve&shy;nire elaboraret, quo commune consequuntur ne. No gubergren prodesset cum, mea alia noster perpetua an, pri nisl fuisset an. No guber&shy;gren prodesset cum, mea alia noster.</p><a href="#">[Read More]</a></div>
</article>

<nav class="abs pager">
  <span class="wide">Prev</span><span class="page">1</span><span class="page">2</span><span class="page">3</span><span class="page">4</span><span class="page">5</span><span class="page">6</span><span class="page">…</span><span class="page">22</span><span class="wide">Next</span>
</nav>

<aside class="abs widget" style="top:1208px;height:372px">
  <div class="widget-head">An Appointment Book</div>
  <div class="field">Name</div>
  <div class="field">Email</div>
  <div class="field">Phone</div>
  <div class="field">Date
    <svg width="18" height="17" viewBox="0 0 18 17" fill="none" stroke="#888" stroke-width="1.2"><rect x="1" y="2.5" width="16" height="13.5"/><path d="M1 6h16M5 1v3M13 1v3M5 9h2M9 9h2M13 9h2M5 12.5h2M9 12.5h2M13 12.5h2"/></svg>
  </div>
  <a class="btn book" href="#">Book Now</a>
</aside>

<aside class="abs widget" style="top:1626px;height:472px">
  <div class="widget-head">Promotional Section
    <svg width="26" height="16" viewBox="0 0 26 16" fill="none" stroke="#fff" stroke-width="2.2"><path d="M7 2l-5 6 5 6M19 2l5 6-5 6"/></svg>
  </div>
  <div class="promo-list">
    <div class="promo-item"><div class="promo-shot"><div role="img" aria-label="Supplement bottle"></div></div><div class="promo-text"><h4>Loreum ipsum dolor</h4><p>Per an dicta clita. Ad idque veniam aliquid sit.</p><a href="#">[View Details]</a></div></div>
    <div class="promo-item"><div class="promo-shot"><div role="img" aria-label="Supplement bottle"></div></div><div class="promo-text"><h4>Loreum ipsum dolor</h4><p>Per an dicta clita. Ad idque veniam aliquid sit.</p><a href="#">[View Details]</a></div></div>
    <div class="promo-item"><div class="promo-shot"><div role="img" aria-label="Supplement bottle"></div></div><div class="promo-text"><h4>Loreum ipsum dolor</h4><p>Per an dicta clita. Ad idque veniam aliquid sit.</p><a href="#">[View Details]</a></div></div>
  </div>
</aside>

<footer class="abs footer">
  <nav class="footer-nav"><a href="#">Home</a><span>/</span><a href="#">About Us</a><span>/</span><a href="#">Products</a><span>/</span><a href="#">Blog</a><span>/</span><a href="#">Contact Us</a></nav>
  <div class="copyright">Copyright @ 2014 Brightleafwell.com.All Rights Reserved.</div>
  <div class="social"><span></span><span></span><span></span><span></span><span></span></div>
</footer>

</body>
</html>
```